Christmas Flyer for Suburban London Cocktail Bar & Party Venue

We need a flyer with details of our Christmas Party drinks packages for party bookings. Tin and Thistle is a local cocktail bar with an emphasis on providing a modern hospitality environment with a sense of fun and whimsy. We pride ourselves on not being generic, providing a community atmosphere and don't take ourselves too seriously and our brand reflects that.

Christmas is one of the most popular times of year and we host parties for many people in our local area. The flyer is intended to summarise our promotional deals and will be distributed to local businesses as well as being available in the bar for customers.

An overview of our mood board that influences 'tone', as we await rebranding, can be seen at https://au.pinboardia.com/korvelmidge/commercial-bar-fit-out-inspiration/

Target Market(s)

21-35 Urban Professionals

Industry/Entity Type

Hospitality

Colors

Designer to choose colors to be used in the design.

Requirements
Must have
• The 4 offers contained in the copy text. Can be adjusted for legibility as long as the offers remain substantively the same.
• The logo of the bar. The standard logo is the gold version however that can be recoloured if appropriate.
• The Address Tin & Thistle - 27 Wrenmoor Rise - Balham, SW7 4KD - This need not be prominent.
Nice to have
• Our social media locations
• facebook /tinandthistlebar
• Instagram /tinandthistlebar
Should not have
• Should not contain photographs or exceptionally generic stock imagery.

```html
<!DOCTYPE html>
<html lang="en">
<head>
<meta charset="utf-8">
<title>Tin &amp; Thistle – Christmas Packages</title>
<link href="https://fonts.googleapis.com/css2?family=Open+Sans:wght@400;600;700&family=Kaushan+Script&display=swap" rel="stylesheet">
<style>
  :root {
    --page-bg: #ebe6de;
    --red-light: #e3222a;
    --red-mid: #b5121b;
    --red-deep: #6e0a10;
    --gold-light: #f3dc8e;
    --gold-mid: #d8b14f;
    --gold-dark: #a7801f;
    --ink-dark: #2a1a0c;
    --badge-red: #b0141c;
    --white: #ffffff;
    --pine-light: #4f9a3a;
    --pine-dark: #1f5a1e;
  }
  * { margin: 0; padding: 0; box-sizing: border-box; }
  html, body { width: 1020px; height: 1200px; overflow: hidden; }
  body {
    background: var(--page-bg);
    font-family: "Open Sans", Arial, sans-serif;
    position: relative;
  }
  .flyer {
    position: absolute; left: 85px; top: 0;
    width: 850px; height: 1200px; overflow: hidden;
    background: radial-gradient(ellipse 70% 45% at 50% 30%, var(--red-light) 0%, var(--red-mid) 55%, var(--red-deep) 100%);
    color: var(--white);
  }
  .bauble-art {
    position: absolute; right: -40px; top: 620px; width: 620px; height: 520px;
    background: radial-gradient(circle at 55% 45%, rgba(150,10,18,0.55) 0%, rgba(110,8,14,0.35) 45%, rgba(110,8,14,0) 70%);
  }
  .pine-art {
    position: absolute; top: 0;
    background: radial-gradient(ellipse at 50% 0%, var(--pine-light) 0%, var(--pine-dark) 55%, rgba(31,90,30,0) 75%);
  }
  .pine-art.left { left: -60px; width: 440px; height: 330px; }
  .pine-art.right { right: -60px; width: 420px; height: 300px; }
  .brand {
    position: absolute; left: 0; width: 850px; top: 225px;
    text-align: center;
    font-family: "Open Sans", Arial, sans-serif; font-weight: 700;
    font-size: 88px; line-height: 1; color: var(--white);
  }
  .badge {
    position: absolute; height: 88px;
    background: linear-gradient(180deg, var(--gold-light) 0%, var(--gold-mid) 55%, var(--gold-dark) 100%);
    border-radius: 6px;
    box-shadow: 0 10px 14px rgba(0,0,0,0.35);
    text-align: center; color: var(--ink-dark);
    padding-top: 13px;
  }
  .badge-title { font-family: "Kaushan Script", cursive; font-size: 28px; line-height: 1.1; }
  .badge-size { font-weight: 700; font-size: 19px; color: var(--badge-red); line-height: 1.3; }
  .badge.solo { padding-top: 25px; }
  .badge-number {
    position: absolute; width: 48px; height: 48px; border-radius: 50%;
    top: 20px; right: -36px;
    background: #2b2b2b; border: 4px solid var(--gold-mid);
    color: var(--white); font-weight: 700; font-size: 25px; line-height: 40px; text-align: center;
  }
  .offer { position: absolute; list-style: none; font-size: 21px; line-height: 28px; white-space: nowrap; }
  .offer li { position: relative; padding-left: 21px; margin-bottom: 4px; }
  .offer li::before {
    content: ""; position: absolute; left: 0; top: 7px;
    border-left: 11px solid var(--gold-light);
    border-top: 7px solid transparent; border-bottom: 7px solid transparent;
  }
  .price { position: absolute; font-weight: 700; font-size: 27px; line-height: 28px; white-space: nowrap; }
  .contact {
    position: absolute; left: 483px; top: 1014px; width: 314px; height: 165px;
    border: 1.5px solid rgba(255,255,255,0.85); border-radius: 10px;
    text-align: center; padding-top: 10px; font-style: normal;
  }
  .address { font-size: 15px; line-height: 1.2; }
  .address svg { vertical-align: -1px; margin-right: 4px; }
  .call-label { font-weight: 700; font-size: 26px; line-height: 1.25; margin-top: 3px; }
  .phone { font-weight: 700; font-size: 29px; line-height: 1.15; }
  .social { font-size: 16px; line-height: 1.3; text-align: left; padding-left: 40px; }
  .social .dot {
    display: inline-block; width: 11px; height: 11px; border-radius: 50%;
    background: var(--white); margin-right: 8px;
  }
  .website {
    position: absolute; left: 59px; top: 1151px; width: 271px; height: 27px;
    border: 1.5px solid rgba(255,255,255,0.85); border-radius: 5px;
    font-size: 15px; line-height: 24px; padding-left: 14px;
  }
  .website .dot {
    display: inline-block; width: 11px; height: 11px; border-radius: 50%;
    border: 1.5px solid var(--white); margin-right: 10px; vertical-align: -1px;
  }
  .package-1 .badge { left: 54px; top: 420px; width: 268px; }
  .package-2 .badge { left: 443px; top: 420px; width: 284px; }
  .package-3 .badge { left: 43px; top: 751px; width: 283px; }
  .package-4 .badge { left: 443px; top: 751px; width: 284px; }
  .package-1 .offer { left: 73px; top: 530px; }
  .package-2 .offer { left: 462px; top: 530px; }
  .package-3 .offer { left: 73px; top: 863px; }
  .package-4 .offer { left: 462px; top: 863px; }
  .package-1 .price { left: 94px; top: 683px; }
  .package-2 .price { left: 483px; top: 683px; }
  .package-3 .price { left: 94px; top: 1087px; }
  .package-4 .price { left: 483px; top: 929px; }
</style>
</head>
<body>
<main class="flyer">
  <div class="bauble-art" role="img" aria-label="Soft-focus red Christmas baubles and pine sprigs"></div>
  <div class="pine-art left" role="img" aria-label="Pine branches with berries and falling snow"></div>
  <div class="pine-art right" role="img" aria-label="Pine branches with red berries and falling snow"></div>

  <h1 class="brand">Tin &amp; Thistle</h1>

  <section class="package package-1">
    <div class="badge">
      <div class="badge-title">Xmas Package</div>
      <div class="badge-size">(10 People)</div>
      <span class="badge-number">1</span>
    </div>
    <ul class="offer">
      <li>10x house spirit + mixer,<br>Glass of wine or prosecco</li>
      <li>10x Cocktails</li>
      <li>10x Beers</li>
      <li>Bottle of prosecco</li>
    </ul>
    <p class="price">£150 - Save up to £65</p>
  </section>

  <section class="package package-2">
    <div class="badge">
      <div class="badge-title">Xmas Package</div>
      <div class="badge-size">(15 People)</div>
      <span class="badge-number">2</span>
    </div>
    <ul class="offer">
      <li>15x house spirit + mixer,<br>Glass of wine or prosecco</li>
      <li>15x Cocktails</li>
      <li>15x Beers</li>
      <li>Sharing cocktail</li>
    </ul>
    <p class="price">£220 - Save up to £85</p>
  </section>

  <section class="package package-3">
    <div class="badge">
      <div class="badge-title">Xmas Package</div>
      <div class="badge-size">(20 People)</div>
      <span class="badge-number">3</span>
    </div>
    <ul class="offer">
      <li>20x house spirit + mixer,<br>Glass of wine or prosecco</li>
      <li>20x Cocktails</li>
      <li>20x Beers</li>
      <li>Bottle of prosecco</li>
      <li>Treasure chest!<br>(12 Person Sharer valued at £100)</li>
    </ul>
    <p class="price">£350 - Save up to £150</p>
  </section>

  <section class="package package-4">
    <div class="badge solo">
      <div class="badge-title">Sharing Combo</div>
    </div>
    <ul class="offer">
      <li>3 of our sharing cocktails</li>
      <li>Bottle of Prosecco</li>
    </ul>
    <p class="price">£85 – Save up to £35</p>
  </section>

  <address class="contact">
    <p class="address">
      <svg width="10" height="14" viewBox="0 0 10 14"><path d="M5 0a5 5 0 0 0-5 5c0 3.6 5 9 5 9s5-5.4 5-9a5 5 0 0 0-5-5zm0 7a2 2 0 1 1 0-4 2 2 0 0 1 0 4z" fill="#fff"/></svg>27 Wrenmoor Rise<br>Balham, SW7 4KD
    </p>
    <p class="call-label">Call Us</p>
    <p class="phone">020 7946 0321</p>
    <p class="social"><span class="dot"></span>facebook /tinandthistlebar</p>
    <p class="social"><span class="dot"></span>Instagram /tinandthistlebar</p>
  </address>

  <p class="website"><span class="dot"></span>www.tinandthistlebar.co.uk</p>
</main>
</body>
</html>
```